Lantern Grove Bridal Show Flyer

I need designed a reusable flyer that is more eye catching than my current flyer. I would also need separate layers as the details change from show to show. I attached the flyer I currently use.

Wedding

```html
<!DOCTYPE html>
<html lang="en">
<head>
<meta charset="utf-8">
<title>Lantern Grove Bridal Show Flyer</title>
<link rel="stylesheet" href="https://fonts.googleapis.com/css2?family=Roboto:wght@400;500;700;900&family=Roboto+Condensed:wght@400;700&family=Roboto+Slab:wght@700&family=Kalam:wght@700&display=swap">
<style>
  :root {
    --sky-top: #dcecf8;
    --sky-mid: #f1f8fd;
    --navy: #16548c;
    --ink-blue: #2470ab;
    --leaf: #9cc25a;
    --leaf-light: #c3de8e;
    --leaf-dark: #2d6a1c;
    --text-dark: #1c2126;
    --white: #ffffff;
    --photo-green: #3f7a32;
    --photo-dark: #1f4a1c;
    --sea: #2b6d9c;
  }
  * { margin: 0; padding: 0; box-sizing: border-box; }
  html, body { width: 1200px; height: 927px; overflow: hidden; background: var(--white); }
  .flyer {
    position: relative; width: 1200px; height: 927px; overflow: hidden;
    font-family: "Roboto", Arial, sans-serif; color: var(--text-dark);
    background:
      radial-gradient(ellipse 520px 380px at 420px 330px, rgba(255,255,255,.9), rgba(255,255,255,0)),
      linear-gradient(180deg, var(--sky-top) 0%, var(--sky-mid) 45%, var(--sky-top) 100%);
  }
  .backdrop { position: absolute; inset: 0; }
  .casting-call {
    position: absolute; left: 159px; top: 38px; font-size: 27px; color: var(--ink-blue); letter-spacing: .3px;
  }
  .show-tab {
    position: absolute; left: 411px; top: 28px; width: 329px; height: 52px;
    background: linear-gradient(180deg, #ffffff, #dcebf7); border-radius: 4px;
    box-shadow: 0 2px 5px rgba(40,80,120,.3);
    font-size: 27px; color: var(--ink-blue); text-align: center; line-height: 52px;
  }
  .show-title {
    position: absolute; left: 186px; top: 122px; width: 491px; text-align: center;
    font-weight: 900; font-size: 60px; line-height: 70px; letter-spacing: 1px;
    color: var(--leaf-dark); text-shadow: 0 0 3px var(--white), 0 3px 4px rgba(0,0,0,.35);
  }
  .prize-lead {
    position: absolute; left: 0; width: 855px; top: 253px; text-align: center; font-size: 28px;
  }
  .prize-amount {
    position: absolute; left: 0; width: 925px; top: 291px; text-align: center;
    font-family: "Roboto Slab", Georgia, serif; font-weight: 700; font-style: italic; font-size: 56px; color: var(--navy);
    text-shadow: 0 2px 3px rgba(22,84,140,.25);
  }
  .show-time {
    position: absolute; left: 0; width: 900px; top: 383px; text-align: center; font-size: 27px;
  }
  .show-time .label { font-weight: 500; color: var(--navy); }
  .venue-card {
    position: absolute; left: 198px; top: 452px; width: 516px; height: 121px;
    background: linear-gradient(180deg, #ffffff, #e9eef3); border: 1px solid #c6d6e4;
    box-shadow: 0 3px 8px rgba(30,60,90,.28); text-align: center;
  }
  .venue-name {
    margin-top: 21px; font-family: "Roboto Condensed", Arial, sans-serif; font-weight: 700; font-size: 34px; color: var(--navy);
  }
  .venue-address { margin-top: 6px; font-size: 27px; color: var(--ink-blue); letter-spacing: .5px; }
  .coupon-band {
    position: absolute; left: 298px; top: 578px; width: 547px; height: 40px;
    background: var(--leaf-light); font-size: 22px; line-height: 40px; padding-left: 42px; color: var(--text-dark);
  }
  .coupon-band strong { font-weight: 700; color: var(--leaf-dark); }
  .giveaway-tag {
    position: absolute; left: 332px; top: 680px; width: 404px; height: 74px;
    background: var(--white); border: 2px solid #cfe0ee; outline: 1px solid var(--ink-blue); outline-offset: -7px;
    transform: rotate(-1.5deg); box-shadow: 0 3px 6px rgba(30,60,90,.25);
    font-family: "Kalam", cursive; font-weight: 700; font-size: 31px; line-height: 74px; text-align: center; color: #111;
  }
  .tickets, .sponsor {
    position: absolute; left: 64px; font-family: "Roboto Condensed", Arial, sans-serif; font-size: 25px;
  }
  .tickets { top: 812px; font-weight: 700; color: var(--navy); text-shadow: 1px 1px 0 rgba(255,255,255,.6); }
  .sponsor { top: 859px; color: var(--white); text-shadow: 1px 1px 2px rgba(10,40,80,.7); }
  .brand-name {
    position: absolute; left: 829px; top: 845px; font-family: "Roboto Condensed", Arial, sans-serif;
    font-size: 40px; color: var(--white);
  }
</style>
</head>
<body>
<main class="flyer">
  <svg class="backdrop" width="1200" height="927" viewBox="0 0 1200 927">
    <defs>
      <linearGradient id="lowerSky" x1="0" y1="0" x2="0" y2="1">
        <stop offset="0" stop-color="#c5e0f3"/>
        <stop offset="1" stop-color="#8ec2e6"/>
      </linearGradient>
      <linearGradient id="gardenTone" x1="0" y1="0" x2="1" y2="1">
        <stop offset="0" stop-color="var(--photo-green)"/>
        <stop offset=".5" stop-color="var(--photo-dark)"/>
        <stop offset="1" stop-color="#5c8f44"/>
      </linearGradient>
      <linearGradient id="seaTone" x1="0" y1="0" x2="0" y2="1">
        <stop offset="0" stop-color="#4f8a4a"/>
        <stop offset=".35" stop-color="var(--sea)"/>
        <stop offset="1" stop-color="#174f7a"/>
      </linearGradient>
      <linearGradient id="ribbonFace" x1="0" y1="0" x2="0" y2="1">
        <stop offset="0" stop-color="#f2f9df"/>
        <stop offset="1" stop-color="#acd16c"/>
      </linearGradient>
    </defs>

    <path class="lower-sky" d="M0,535 C250,640 560,760 840,790 L1200,800 L1200,927 L0,927 Z" fill="url(#lowerSky)"/>
    <path class="grey-sweep" d="M40,530 C150,640 300,720 460,765" stroke="#b9c4cc" stroke-width="3" fill="none"/>

    <path class="leaf-curve" d="M1000,0 C915,70 845,210 865,330 C882,440 885,540 850,640 C830,700 800,760 760,800 L840,800 C870,740 895,650 905,560 C920,430 905,320 930,220 C955,120 1010,40 1070,0 Z" fill="var(--leaf)"/>
    <path class="navy-swoosh" d="M30,625 C300,760 600,800 900,790 C1000,785 1100,790 1200,795 L1200,810 C1000,805 850,815 700,812 C450,805 220,740 30,625 Z" fill="var(--navy)"/>
    <path class="navy-curve" d="M905,430 C900,560 880,680 830,790 L870,790 C900,690 915,560 905,430 Z" fill="var(--navy)"/>

    <path class="bride-photo" role="img" aria-label="Photo of a smiling bride in a strapless white gown with a birdcage veil, standing in a leafy garden" d="M1015,0 C945,70 890,200 905,320 C918,430 920,540 890,650 C875,710 860,760 845,795 L1200,795 L1200,0 Z" fill="url(#gardenTone)"/>

    <rect class="bottom-band" x="0" y="800" width="1200" height="127" fill="#8ec2e6" opacity=".55"/>

    <rect class="frame" x="20" y="18" width="1162" height="888" fill="none" stroke="#6d9cc2" stroke-width="1.2" opacity=".7"/>

    <g class="title-ribbon">
      <path d="M118,141 L200,141 L200,227 L118,227 L160,184 Z" fill="#c9e29a"/>
      <path d="M745,141 L663,141 L663,227 L745,227 L703,184 Z" fill="#c9e29a"/>
      <path d="M186,202 L216,227 L216,202 Z" fill="#5a6470"/>
      <path d="M677,202 L647,227 L647,202 Z" fill="#5a6470"/>
      <rect x="186" y="114" width="491" height="88" fill="url(#ribbonFace)" stroke="#a9cc6b" stroke-width="2"/>
    </g>

    <g class="prize-rules" stroke="#9fb9cf" stroke-width="1.5">
      <line x1="150" y1="327" x2="372" y2="327"/>
      <line x1="180" y1="335" x2="365" y2="335"/>
      <line x1="560" y1="327" x2="750" y2="327"/>
      <line x1="565" y1="335" x2="720" y2="335"/>
    </g>

    <ellipse class="cruise-frame" cx="218" cy="714" rx="166" ry="76" fill="var(--white)"/>
    <ellipse class="cruise-photo" role="img" aria-label="Photo of a white cruise ship sailing past a green island on blue water" cx="218" cy="714" rx="156" ry="67" fill="url(#seaTone)"/>
  </svg>

  <p class="casting-call">Open Casting Call</p>
  <p class="show-tab">Find the One Gown</p>
  <h1 class="show-title">BRIDAL SHOW</h1>

  <p class="prize-lead">The first 50 brides will get a chance to win</p>
  <p class="prize-amount">$25,000</p>
  <p class="show-time"><span class="label">When:</span> Tuesday, September 16th &nbsp;·&nbsp; 6:00–9:00 PM</p>

  <section class="venue-card">
    <h2 class="venue-name">The Harbor Terrace at Bellamy’s</h2>
    <p class="venue-address">1190 Shoreline Avenue, Milford, CT</p>
  </section>
  <p class="coupon-band">$3 off admission with coupon code <strong>NP3</strong></p>

  <p class="giveaway-tag">Honeymoon Cruise Giveaway</p>

  <p class="tickets">Get Tickets at lanterngrove-events.com - 203-555-0148</p>
  <p class="sponsor">Sponsored by: Moonlit Rhythm Entertainment</p>
  <p class="brand-name">Lantern Grove</p>
</main>
</body>
</html>
```